Stylish business cards for TX9

To create an appealing and professional business card design for a WOMEN Owned Construction Supply Company.
2 sided card. Incorporate brand elements, curvy, colorful, sleek and bright. No solid white background. attached samples of styles added shapes/ribbons. Want something with that WOW that looks awesome, factor. It is a new logo, so feel free to mess with logo colors in the blue and teal factors that can look good with both dark and light background. If you want to try a watermark with just the TX9, without the "Supply" that might look cool to.

Industry/Entity Type

Women owned construction supply company

Contact Information for Business Card

Name, Title, and phone number and email, web page. maybe spot for qr code.

Font styles to use
Sans Serif

Requirements
Nice to have
• would love to see colors, maybe stylish ribbon dividers or some sort of 2 or 3 tone color card that compliments logo.
Should not have
• Please do not have all white background. Do not include Home/reale state/ or building images.

```html
<!DOCTYPE html>
<html lang="en">
<head>
<meta charset="utf-8">
<title>TX9 Supply – Business Card</title>
<link rel="stylesheet" href="https://fonts.googleapis.com/css2?family=Montserrat:wght@400;500;700&display=swap">
<style>
  :root {
    --stage: #1c1c1c;
    --navy: #1a3a5c;
    --teal: #2494bd;
    --paper: #f3f3f3;
    --ink-soft: #3c3c3c;
    --radius: 15px;
  }
  * { margin: 0; padding: 0; box-sizing: border-box; }
  html, body { width: 1200px; height: 1059px; overflow: hidden; }
  body {
    background: var(--stage);
    font-family: "Montserrat", Arial, sans-serif;
    position: relative;
  }
  .card {
    position: absolute;
    left: 256px;
    width: 690px;
    height: 392px;
    border-radius: var(--radius);
    overflow: hidden;
  }
  .card--front { top: 89px; background: var(--paper); }
  .card--back { top: 547px; background: var(--navy); }

  .front-sweep { position: absolute; inset: 0; width: 100%; height: 100%; }

  .wordmark { font-weight: 700; letter-spacing: 0.5px; white-space: nowrap; }
  .card--front .wordmark {
    position: absolute; left: 29px; top: 82px;
    font-size: 32px; color: var(--navy);
  }
  .card--back .wordmark {
    position: absolute; left: 0; right: 0; top: 160px;
    text-align: center; font-size: 60px; color: #ffffff;
  }

  .name-bar {
    position: absolute; left: 0; top: 193px;
    width: 17px; height: 36px; background: var(--navy);
  }
  .holder { position: absolute; left: 29px; top: 190px; }
  .holder__name {
    font-size: 22px; font-weight: 700; color: var(--navy); line-height: 1.15;
  }
  .holder__title { font-size: 15px; color: var(--ink-soft); line-height: 1.3; }

  .contacts {
    position: absolute; left: 29px; top: 247px;
    list-style: none; font-size: 15px; color: var(--ink-soft);
  }
  .contacts li {
    display: flex; align-items: flex-start; gap: 7px;
    line-height: 22px; margin-bottom: 2px;
  }
  .contacts svg { flex: none; width: 13px; height: 13px; margin-top: 5px; fill: var(--teal); }
</style>
</head>
<body>

<section class="card card--front">
  <svg class="front-sweep" viewBox="0 0 690 392" preserveAspectRatio="none" aria-hidden="true">
    <path d="M447 0 C512 92 506 290 331 392 L690 392 L690 0 Z" fill="var(--teal)"/>
    <path d="M470 0 C528 100 516 280 368 392 L690 392 L690 0 Z" fill="#ffffff"/>
    <path d="M475 0 C535 105 522 282 380 392 L690 392 L690 0 Z" fill="var(--navy)"/>
    <path d="M505 42 C522 140 505 290 378 392 L398 392 C505 300 520 160 505 42 Z" fill="var(--teal)"/>
  </svg>

  <div class="wordmark">TX9 Supply</div>

  <div class="name-bar"></div>
  <div class="holder">
    <p class="holder__name">DANA WHITLOW</p>
    <p class="holder__title">CEO/Founder</p>
  </div>

  <ul class="contacts">
    <li>
      <svg viewBox="0 0 24 24"><path d="M6.6 10.8a15 15 0 0 0 6.6 6.6l2.2-2.2a1 1 0 0 1 1-.25 11.4 11.4 0 0 0 3.6.57 1 1 0 0 1 1 1V20a1 1 0 0 1-1 1A17 17 0 0 1 3 4a1 1 0 0 1 1-1h3.5a1 1 0 0 1 1 1c0 1.25.2 2.45.57 3.57a1 1 0 0 1-.25 1z"/></svg>
      <span>555.014.2287</span>
    </li>
    <li>
      <svg viewBox="0 0 24 24"><path d="M2 5h20v14H2z M2 5l10 8 10-8" fill="var(--teal)"/><path d="M3 6l9 7 9-7" stroke="#f3f3f3" stroke-width="1.5" fill="none"/></svg>
      <span>info@tx9supply.com.au</span>
    </li>
    <li>
      <svg viewBox="0 0 24 24"><circle cx="12" cy="12" r="10" fill="none" stroke="var(--teal)" stroke-width="2"/><ellipse cx="12" cy="12" rx="4" ry="10" fill="none" stroke="var(--teal)" stroke-width="2"/><path d="M2 12h20M4 7h16M4 17h16" stroke="var(--teal)" stroke-width="1.6"/></svg>
      <span>www.tx9supply.com.au</span>
    </li>
    <li>
      <svg viewBox="0 0 24 24"><path d="M12 1a8 8 0 0 0-8 8c0 6 8 14 8 14s8-8 8-14a8 8 0 0 0-8-8zm0 11a3 3 0 1 1 0-6 3 3 0 0 1 0 6z"/></svg>
      <span>P.O Box 4170 Harbour Lane Road<br>Westfield CD 40210</span>
    </li>
  </ul>
</section>

<section class="card card--back">
  <div class="wordmark">TX9 Supply</div>
</section>

</body>
</html>
```